Custom Home Builder Website

We need a re-design of a website for our client: "http://www.tovarelbuilds.com". Their current design is outdated and has flash. We need to make it responsive for all devices and with a more professional look.

Pages to consider:
1. Home page
2. Portfolio page - gallery of projects (multiple images of a project with captions, and a main text area for each project).

Good clean design reflecting quality craftsmanship is a must.

We only need designs, no coding required

Target Market(s)

The intended market is home owners looking to build with a reputable and professional home builder.

Industry/Entity Type

Home Builder

Requirements
Must have
• Must Have:
• - main areas of site: home, portfolio, video gallery, contact
Nice to have
• - Maybe pullquotes from testimonials placed as slideshow?

```html
<!DOCTYPE html>
<html lang="en">
<head>
<meta charset="utf-8">
<title>Tovarel Built — Portfolio</title>
<link rel="stylesheet" href="https://fonts.googleapis.com/css2?family=Arimo&family=Open+Sans:wght@400;600&family=Tinos&display=swap">
<style>
  :root {
    --page-tan: #c69c6d;
    --bar-dark: #2a1f18;
    --logo-dark: #333130;
    --logo-light: #e6e4e2;
    --brand-tan: #a88a68;
    --card-bg: #f2f2f2;
    --text-grey: #444;
    --accent-red: #f45b52;
    --accent-teal: #6cc3d5;
    --accent-orange: #efa62e;
    --accent-green: #69b96a;
    --icon-grey: #3b3735;
    --photo-living: #a4825e;
    --photo-bedroom: #b3aea6;
    --photo-exterior: #5e5c4a;
    --photo-entry: #8f8882;
    --white: #ffffff;
  }
  * { margin: 0; padding: 0; box-sizing: border-box; }
  html, body { width: 1024px; height: 1200px; overflow: hidden; }
  body { position: relative; background: var(--page-tan); font-family: "Arimo", Arial, sans-serif; }

  .site-header { position: absolute; top: 0; left: 0; width: 1024px; height: 70px; background: var(--bar-dark); }
  .brand { position: absolute; top: 0; left: 0; width: 260px; height: 120px; background: var(--logo-light); z-index: 2; }
  .brand-top { height: 70px; background: var(--logo-dark); }
  .brand-name { position: absolute; left: 26px; top: 16px; width: 210px; text-align: center;
    font-family: "Tinos", serif; font-size: 44px; line-height: 52px; letter-spacing: 1px; color: var(--brand-tan); }
  .brand-name span { display: block; font-size: 24px; line-height: 34px; letter-spacing: 12px; }

  .main-nav { position: absolute; left: 424px; top: 28px; display: flex; gap: 28px; }
  .main-nav a { color: var(--white); text-decoration: none; font-size: 14px; letter-spacing: .2px; }
  .social { position: absolute; right: 24px; top: 20px; display: flex; gap: 15px; }
  .social span { width: 32px; height: 32px; border-radius: 50%; background: var(--icon-grey); display: block; }

  .phone-badge { position: absolute; left: 774px; top: 80px; width: 250px; height: 50px; background: rgba(42,31,24,.92);
    border-radius: 6px 0 0 6px; display: flex; align-items: center; padding-left: 18px; gap: 14px; z-index: 3; }
  .phone-badge p { font-family: "Tinos", serif; font-size: 23px; letter-spacing: 1.5px; color: #e8e4df; }

  .project { position: absolute; width: 400px; height: 450px; background: var(--card-bg); box-shadow: -4px 4px 10px rgba(0,0,0,.35); }
  .project-photo { height: 264px; position: relative; }
  .project-stripe { height: 4px; }
  .project-label { position: absolute; left: 25px; right: 25px; bottom: 3px; height: 26px; background: rgba(20,18,16,.88);
    color: var(--white); font-family: "Open Sans", sans-serif; font-size: 11px; line-height: 26px; text-align: center; }
  .project-text { margin: 8px 9px 0; font-family: "Tinos", serif; font-size: 10.7px; line-height: 14.5px; letter-spacing: -0.1px;
    color: var(--text-grey); text-align: justify; }
  .read-more { position: absolute; left: 121px; top: 401px; width: 162px; height: 24px; background: var(--accent-red);
    color: var(--white); font-family: "Open Sans", sans-serif; font-size: 11px; line-height: 24px; text-align: center; text-decoration: none; }

  .p1 { left: 65px; top: 100px; } .p2 { left: 545px; top: 100px; }
  .p3 { left: 65px; top: 600px; } .p4 { left: 545px; top: 600px; }
  .p1 .project-photo { background: var(--photo-living); }
  .p2 .project-photo { background: var(--photo-bedroom); }
  .p3 .project-photo { background: var(--photo-exterior); }
  .p4 .project-photo { background: var(--photo-entry); }
  .p1 .project-stripe { background: var(--accent-red); }
  .p2 .project-stripe { background: var(--accent-teal); }
  .p3 .project-stripe { background: var(--accent-orange); }
  .p4 .project-stripe { background: var(--accent-green); }

  .site-footer { position: absolute; left: 0; top: 1130px; width: 1024px; height: 70px; background: var(--bar-dark); color: #d8d2cb; }
  .footer-address { position: absolute; left: 150px; top: 10px; font-family: "Open Sans", sans-serif; font-size: 11px; }
  .footer-copy { position: absolute; left: 118px; top: 35px; font-family: "Tinos", serif; font-size: 12px; }
  .footer-nav { position: absolute; left: 375px; top: 34px; display: flex; gap: 30px; }
  .footer-nav a { color: var(--white); text-decoration: none; font-size: 14px; }
</style>
</head>
<body>
  <header class="site-header">
    <div class="brand">
      <div class="brand-top"></div>
      <div class="brand-name">TOVAREL<span>BUILT</span></div>
    </div>
    <nav class="main-nav">
      <a href="#">HOME</a><a href="#">PORTFOLIO</a><a href="#">GALLERY</a><a href="#">NEWS</a><a href="#">CONTACT</a>
    </nav>
    <div class="social" aria-label="Social links"><span></span><span></span><span></span></div>
  </header>

  <div class="phone-badge">
    <svg width="32" height="32" viewBox="0 0 24 24" aria-hidden="true"><path fill="#e8e4df" d="M6.6 10.8a15.1 15.1 0 0 0 6.6 6.6l2.2-2.2c.3-.3.7-.4 1-.2 1.1.4 2.3.6 3.6.6.6 0 1 .4 1 1V20c0 .6-.4 1-1 1A17 17 0 0 1 3 4c0-.6.4-1 1-1h3.5c.6 0 1 .4 1 1 0 1.3.2 2.5.6 3.6.1.3 0 .7-.2 1z"/></svg>
    <p>(503) 555-0187</p>
  </div>

  <main>
    <article class="project p1">
      <div class="project-photo" role="img" aria-label="Photo: living room with fireplace and large windows onto autumn trees"><div class="project-label">PROJECT 1</div></div>
      <div class="project-stripe"></div>
      <p class="project-text">Lorem ipsum dolor sit amet, consectetur adipisicing elit, sed do eiusmod tempor incididunt ut labore et dolore magna aliqua. Ut enim ad minim veniam, quis nostrud exercitation ullamco laboris nisi ut aliquip ex ea commodo consequat. Duis aute irure dolor in reprehenderit in voluptate velit esse cillum dolore eu fugiat nulla pariatur. Excepteur sint occaecat cupidatat non proident, sunt in culpa qui officia deserunt mollit anim id est laborum.</p>
      <a class="read-more" href="#">READ MORE</a>
    </article>
    <article class="project p2">
      <div class="project-photo" role="img" aria-label="Photo: bright children's bedroom with dresser and window"><div class="project-label">PROJECT 2</div></div>
      <div class="project-stripe"></div>
      <p class="project-text">Lorem ipsum dolor sit amet, consectetur adipisicing elit, sed do eiusmod tempor incididunt ut labore et dolore magna aliqua. Ut enim ad minim veniam, quis nostrud exercitation ullamco laboris nisi ut aliquip ex ea commodo consequat. Duis aute irure dolor in reprehenderit in voluptate velit esse cillum dolore eu fugiat nulla pariatur. Excepteur sint occaecat cupidatat non proident, sunt in culpa qui officia deserunt mollit anim id est laborum.</p>
      <a class="read-more" href="#">READ MORE</a>
    </article>
    <article class="project p3">
      <div class="project-photo" role="img" aria-label="Photo: two-storey home exterior among tall evergreen trees"><div class="project-label">PROJECT 3</div></div>
      <div class="project-stripe"></div>
      <p class="project-text">Lorem ipsum dolor sit amet, consectetur adipisicing elit, sed do eiusmod tempor incididunt ut labore et dolore magna aliqua. Ut enim ad minim veniam, quis nostrud exercitation ullamco laboris nisi ut aliquip ex ea commodo consequat. Duis aute irure dolor in reprehenderit in voluptate velit esse cillum dolore eu fugiat nulla pariatur. Excepteur sint occaecat cupidatat non proident, sunt in culpa qui officia deserunt mollit anim id est laborum.</p>
      <a class="read-more" href="#">READ MORE</a>
    </article>
    <article class="project p4">
      <div class="project-photo" role="img" aria-label="Photo: entry hall with wooden front door beside a dining area"><div class="project-label">PROJECT 4</div></div>
      <div class="project-stripe"></div>
      <p class="project-text">Lorem ipsum dolor sit amet, consectetur adipisicing elit, sed do eiusmod tempor incididunt ut labore et dolore magna aliqua. Ut enim ad minim veniam, quis nostrud exercitation ullamco laboris nisi ut aliquip ex ea commodo consequat. Duis aute irure dolor in reprehenderit in voluptate velit esse cillum dolore eu fugiat nulla pariatur. Excepteur sint occaecat cupidatat non proident, sunt in culpa qui officia deserunt mollit anim id est laborum.</p>
      <a class="read-more" href="#">READ MORE</a>
    </article>
  </main>

  <footer class="site-footer">
    <p class="footer-address">4820 NW ALDER RIDGE RD, # 210, CEDAR FALLS, OR 97301</p>
    <p class="footer-copy">© 2013 TOVAREL CUSTOM HOMES</p>
    <nav class="footer-nav">
      <a href="#">HOME</a><a href="#">PORTFOLIO</a><a href="#">GALLERY</a><a href="#">NEWS</a><a href="#">CONTACT US</a>
    </nav>
  </footer>
</body>
</html>
```